Weight Loss Challenge Social Media Graphics

Create 6-7 individual social media graphics (square size) to encourage folks to join our weight loss challenge. For the color scheme of the graphics, use the color palette attached

Note: each graphic can contain any of the stock photography attached or just the single picture of me (brown shirt) but a few should be ONLY the text
For some graphics we can say: JOIN US!
For some graphics, use only TEXT based

Target Market(s)

primarily women who want to get healthy

Industry/Entity Type

health and weight loss

Requirements
Must have
• The largest text should be: Ninety Days Bold

```html
<!DOCTYPE html>
<html lang="en">
<head>
<meta charset="utf-8">
<title>Ninety Days Bold – Social Graphics</title>
<link href="https://fonts.googleapis.com/css2?family=Oswald:wght@400;500;600;700&family=Cinzel:wght@400;600&family=Archivo+Black&family=Allura&family=Montserrat:wght@400;600&display=swap" rel="stylesheet">
<style>
:root{
  --sheet:#ffffff;
  --label:#4a4a4a;
  --pink:#f4b8cb;
  --pink-light:#f9dbe6;
  --brown:#8b5a3c;
  --tan:#d2a27f;
  --ink:#231c1c;
  --cream:#f3e0d0;
  --mauve:#b69189;
  --mauve-dark:#9d7a72;
  --choc:#6e4330;
  --choc-dark:#4a2c20;
  --photo-blue:#a9c6dc;
  --photo-warm:#b88a6e;
  --photo-soft:#d9b8b0;
}
*{box-sizing:border-box;margin:0;padding:0}
html,body{width:1200px;height:1200px;overflow:hidden;background:var(--sheet)}
.sheet{position:relative;width:1200px;height:1200px}
.label{position:absolute;width:120px;text-align:center;font:700 46px/1 "Oswald",sans-serif;color:var(--label)}
.card{position:absolute;width:380px;height:380px;overflow:hidden;box-shadow:0 18px 22px -14px rgba(0,0,0,.35)}
.photo{position:absolute}
.abs{position:absolute}

/* card 1 */
.c1{background:var(--pink)}
.c1 .side{left:220px;top:0;width:160px;height:122px;background:var(--pink-light)}
.c1 .side-b{left:220px;top:300px;width:160px;height:80px;background:var(--pink-light)}
.c1 .title{left:20px;top:22px;font-family:"Cinzel",serif;color:var(--brown)}
.c1 .title .small{font-size:22px;line-height:1}
.c1 .title .big{font-size:58px;line-height:1}
.c1 .chal{left:248px;top:16px;width:118px;font:400 16px/1 "Cinzel",serif;color:var(--brown);border-bottom:1px solid #6b6fa0;padding-bottom:4px}
.c1 .lose{left:248px;top:60px;font:400 11px/1.05 "Cinzel",serif;color:var(--ink)}
.c1 .frame{left:58px;top:138px;width:270px;height:172px;background:#fff;transform:rotate(-5deg);padding:9px}
.c1 .frame .photo{position:relative;width:100%;height:100%;background:linear-gradient(135deg,var(--photo-blue),#e8c7b8)}
.c1 .begins{left:12px;top:352px;font:400 12px/1 "Cinzel",serif;color:var(--ink)}
.c1 .join{left:232px;top:338px;font:400 30px/1 "Cinzel",serif;color:var(--brown)}

/* card 2 */
.c2{background:#fff}
.c2 .photo{left:14px;top:4px;width:160px;height:290px;border-radius:80px 80px 40px 40px;background:linear-gradient(180deg,var(--tan),#c99172 60%,var(--ink))}
.c2 .t1{left:186px;top:34px;font:500 33px/1 "Oswald",sans-serif;color:var(--tan);white-space:nowrap}
.c2 .t2{left:206px;top:66px;font:400 68px/1 "Allura",cursive;color:var(--ink)}
.c2 .chal{left:186px;top:162px;width:170px;font:500 17px/1 "Oswald",sans-serif;color:var(--tan);border-bottom:1px solid var(--tan);padding-bottom:8px;white-space:nowrap}
.c2 .lose{left:186px;top:202px;font:500 17px/1.1 "Oswald",sans-serif;color:var(--tan);white-space:nowrap}
.c2 svg{position:absolute;left:0;top:250px}
.c2 .badge{left:90px;top:285px;width:100px;height:80px;border-radius:50%;background:var(--tan);border:1px dashed #fff;transform:rotate(-30deg);display:flex;align-items:center;justify-content:center;font:500 24px/1 "Oswald",sans-serif;color:#fff}
.c2 .begins{left:218px;top:308px;font:500 23px/1.05 "Oswald",sans-serif;color:var(--tan)}

/* card 3 */
.c3{background:var(--cream)}
.c3 .title{left:38px;top:8px;font-family:"Oswald",sans-serif;color:var(--choc);font-weight:600}
.c3 .title .small{font-size:32px;line-height:1}
.c3 .title .big{font-size:72px;line-height:.95}
.c3 .rule{left:260px;top:22px;width:1px;height:82px;background:var(--choc)}
.c3 .begins{left:276px;top:22px;font:600 27px/.95 "Oswald",sans-serif;color:var(--choc)}
.c3 .strip{top:118px;width:58px;height:186px;background:linear-gradient(180deg,var(--photo-warm),var(--choc-dark))}
.c3 .band{left:0;top:300px;width:380px;height:80px;background:var(--choc)}
.c3 .line{left:0;top:310px;width:380px;text-align:center;font:600 12px/1 "Oswald",sans-serif;color:#fff}
.c3 .join{left:0;top:328px;width:380px;text-align:center;font:400 40px/1 "Archivo Black",sans-serif;color:var(--cream);letter-spacing:2px}

/* card 4 */
.c4{background:var(--cream)}
.c4 .stripe{top:0;height:380px}
.c4 .title{left:38px;top:8px;font-family:"Oswald",sans-serif;color:#000;font-weight:700}
.c4 .title .small{font-size:36px;line-height:1}
.c4 .title .big{font-size:78px;line-height:.95}
.c4 .begins{left:276px;top:20px;font:600 30px/.92 "Oswald",sans-serif;color:#000}
.c4 .photo{left:0;top:126px;width:380px;height:185px;background:linear-gradient(90deg,#d8c2b2,#c9a6a4 40%,#b48a98 65%,#e3c3c0);opacity:.85}
.c4 .line{left:0;top:316px;width:380px;text-align:center;font:600 12px/1 "Oswald",sans-serif;color:#000}
.c4 .join{left:0;top:330px;width:380px;text-align:center;font:400 38px/1 "Archivo Black",sans-serif;color:#000;letter-spacing:2px}
.c4 .base{left:0;top:374px;width:380px;height:2px;background:#7d6a66}

/* card 5 */
.c5{background:#f7f5f5}
.c5 .title{left:0;top:16px;width:380px;text-align:center;font:400 38px/1 "Archivo Black",sans-serif;color:var(--mauve);letter-spacing:1px}
.c5 .band{top:102px;height:190px}
.c5 .circle{position:absolute;border-radius:50%;border:2px solid #fff}
.c5 .chal{left:300px;top:136px;font:600 11px/1.1 "Oswald",sans-serif;color:var(--ink)}
.c5 .lose{left:8px;top:230px;font:600 11px/1.1 "Oswald",sans-serif;color:var(--ink)}
.c5 .begins{left:0;top:298px;width:380px;text-align:center;font:400 20px/1 "Archivo Black",sans-serif;color:var(--mauve)}
.c5 .join{left:0;top:322px;width:380px;text-align:center;font:400 42px/1 "Archivo Black",sans-serif;color:var(--mauve);letter-spacing:2px}

/* card 6 */
.c6{background:#fff}
.c6 .hero{left:240px;top:0;width:140px;height:380px;background:linear-gradient(180deg,#e9e2dc,var(--tan) 55%,var(--ink))}
.c6 .badge{left:26px;top:10px;width:80px;height:212px;border-radius:40px;background:var(--mauve);display:flex;flex-direction:column;align-items:center;justify-content:center;font:400 15px/1.15 "Archivo Black",sans-serif;color:var(--ink);text-align:center}
.c6 .badge .big{font-size:22px}
.c6 .ticks{left:16px;top:240px;width:120px;font:400 8.5px/1.2 "Montserrat",sans-serif;color:#555;list-style:none}
.c6 .ticks li{position:relative;padding:4px 0 4px 11px;border-bottom:1px solid #ddd}
.c6 .ticks li.one{white-space:nowrap}
.c6 .ticks li::before{content:"✓";position:absolute;left:0;top:4px;color:var(--mauve)}
.c6 .thumb{left:140px;width:118px;height:72px}
.c6 .band{left:0;top:330px;width:260px;height:50px;background:var(--mauve)}
.c6 .join{left:14px;top:332px;font:400 36px/1.2 "Archivo Black",sans-serif;color:#000}
</style>
</head>
<body>
<div class="sheet">
  <div class="label" style="left:126px;top:68px">01</div>
  <div class="label" style="left:558px;top:68px">02</div>
  <div class="label" style="left:936px;top:68px">03</div>
  <div class="label" style="left:130px;top:616px">04</div>
  <div class="label" style="left:558px;top:616px">05</div>
  <div class="label" style="left:936px;top:616px">06</div>

  <section class="card c1" style="left:26px;top:151px">
    <div class="abs side"></div><div class="abs side-b"></div>
    <div class="abs title"><div class="small">NINETY DAYS</div><div class="big">BOLD</div></div>
    <div class="abs chal">45 STRONG CHALLENGE</div>
    <div class="abs lose">LOSE UP TO<br>20 POUNDS<br>IN 6 WEEKS!</div>
    <div class="abs frame"><div class="photo" role="img" aria-label="Group of smiling adults flexing their arms in a bright gym"></div></div>
    <div class="abs begins">BEGINS MONDAY JAN 6<sup>TH</sup></div>
    <div class="abs join">JOIN US!</div>
  </section>

  <section class="card c2" style="left:415px;top:151px">
    <div class="photo" role="img" aria-label="Smiling coach in a tan turtleneck and black leggings, hand on hip"></div>
    <div class="abs t1">NINETY DAYS</div>
    <div class="abs t2">Bold</div>
    <div class="abs chal">45 STRONG CHALLENGE</div>
    <div class="abs lose">LOSE UP TO 20 POUNDS<br>IN 6 WEEKS!</div>
    <svg width="380" height="130" viewBox="0 0 380 130"><path d="M0 90 C60 70 110 95 170 88 C240 80 270 10 330 10 C355 10 370 20 380 30 L380 130 L0 130 Z" fill="var(--ink)" stroke="var(--tan)" stroke-width="3"/></svg>
    <div class="abs badge">JOIN US!</div>
    <div class="abs begins">BEGINS MONDAY<br>JAN 6<sup>TH</sup></div>
  </section>

  <section class="card c3" style="left:804px;top:151px">
    <div class="abs title"><div class="small">NINETY DAYS</div><div class="big">BOLD</div></div>
    <div class="abs rule"></div>
    <div class="abs begins">BEGINS<br>MONDAY<br>JAN 6<sup>TH</sup></div>
    <div class="abs strip photo" style="left:40px" role="img" aria-label="Woman in a black top, arms crossed"></div>
    <div class="abs strip photo" style="left:101px" role="img" aria-label="Woman in a black top smiling"></div>
    <div class="abs strip photo" style="left:162px" role="img" aria-label="Woman in a black top, hand at chin"></div>
    <div class="abs strip photo" style="left:223px" role="img" aria-label="Woman in a black top, arms crossed"></div>
    <div class="abs strip photo" style="left:284px" role="img" aria-label="Woman in a black top with curly hair"></div>
    <div class="abs band"></div>
    <div class="abs line">45 STRONG CHALLENGE | LOSE UP TO 20 POUNDS IN 6 WEEKS!</div>
    <div class="abs join">JOIN US!</div>
  </section>

  <section class="card c4" style="left:26px;top:700px">
    <div class="abs stripe" style="left:64px;width:63px;background:var(--mauve)"></div>
    <div class="abs stripe" style="left:127px;width:63px;background:#d4a8a8"></div>
    <div class="abs stripe" style="left:190px;width:127px;background:var(--pink)"></div>
    <div class="abs stripe" style="left:317px;width:63px;background:var(--pink-light)"></div>
    <div class="abs title"><div class="small">NINETY DAYS</div><div class="big">BOLD</div></div>
    <div class="abs begins">BEGINS<br>MONDAY<br>JAN 6<sup>TH</sup></div>
    <div class="photo" role="img" aria-label="Four women in sports bras and leggings laughing together"></div>
    <div class="abs line">45 STRONG CHALLENGE | LOSE UP TO 20 POUNDS IN 6 WEEKS!</div>
    <div class="abs join">JOIN US!</div>
    <div class="abs base"></div>
  </section>

  <section class="card c5" style="left:415px;top:700px">
    <div class="abs title">NINETY DAYS<br>BOLD</div>
    <div class="abs band" style="left:0;width:64px;background:var(--cream)"></div>
    <div class="abs band" style="left:64px;width:126px;background:var(--mauve-dark)"></div>
    <div class="abs band" style="left:190px;width:64px;background:#d4a8a8"></div>
    <div class="abs band" style="left:254px;width:126px;background:var(--pink)"></div>
    <div class="circle" style="left:52px;top:118px;width:112px;height:112px;background:linear-gradient(135deg,var(--photo-blue),#e0c0b5)" role="img" aria-label="Group of adults flexing in a gym"></div>
    <div class="circle" style="left:208px;top:114px;width:82px;height:82px;background:linear-gradient(135deg,#d8c6d0,#b4909e)" role="img" aria-label="Women in sports bras laughing"></div>
    <div class="circle" style="left:156px;top:210px;width:74px;height:74px;background:linear-gradient(135deg,var(--photo-warm),var(--choc-dark))" role="img" aria-label="Women in black tops"></div>
    <div class="circle" style="left:262px;top:180px;width:106px;height:106px;background:linear-gradient(135deg,#a87860,var(--ink))" role="img" aria-label="Group of women in black and white activewear"></div>
    <div class="abs chal">45 STRONG<br>CHALLENGE</div>
    <div class="abs lose">LOSE UP TO<br>20 POUNDS<br>IN 6 WEEKS!</div>
    <div class="abs begins">BEGINS MONDAY JAN 6<sup>TH</sup></div>
    <div class="abs join">JOIN US!</div>
  </section>

  <section class="card c6" style="left:804px;top:700px">
    <div class="abs hero photo" role="img" aria-label="Smiling coach in a tan turtleneck and black jeans"></div>
    <div class="abs badge"><span>NINETY</span><span>DAYS</span><span class="big">BOLD</span></div>
    <ul class="abs ticks">
      <li class="one">45 Strong Challenge</li>
      <li>Lose Up To 20 Pounds<br>In 6 Weeks!</li>
      <li class="one">Begins Monday Jan 6<sup>th</sup></li>
    </ul>
    <div class="abs thumb photo" style="top:12px;background:linear-gradient(135deg,var(--photo-blue),#e0c0b5)" role="img" aria-label="Group of adults flexing in a gym"></div>
    <div class="abs thumb photo" style="top:90px;background:linear-gradient(135deg,var(--photo-warm),var(--choc-dark))" role="img" aria-label="Women in black tops"></div>
    <div class="abs thumb photo" style="top:168px;background:linear-gradient(135deg,#a87860,var(--ink))" role="img" aria-label="Women in black and white activewear"></div>
    <div class="abs thumb photo" style="top:246px;background:linear-gradient(135deg,#d8c6d0,#b4909e)" role="img" aria-label="Women in sports bras and leggings"></div>
    <div class="abs band"></div>
    <div class="abs join">JOIN US!</div>
  </section>
</div>
</body>
</html>
```